Mattress sale flyer front and back

FLYER SIZE!! front and back!
4.25" X 5.5"
or
10.7cm X 13.9 cm

This flyer needs to show the prices
twin.....$99
full.......$159
queen...$199
king....$299

the phone number........(786)413-9072
the address ..........24315 sw 142st miami fl 33157
if possible a map would be appreciated

possible brands to include.......Dravo, Quillard, brook & vantle, plumnight

ATTACHED IS OUR OLD FLYER WITH OUTDATED INFORMATION, I WOULD LIKE SOMETHING SIMILAR. JUST ADD A LITTLE PRICE LIST AND A MAP

***FRONT AND BACK PLEASE****

```html
<!DOCTYPE html>
<html lang="en">
<head>
<meta charset="utf-8">
<title>Coral Rest Outlet – Flyer Front and Back</title>
<link rel="stylesheet" href="https://fonts.googleapis.com/css2?family=Oswald:wght@400;500;600;700&display=swap">
<style>
  :root {
    --yellow: #ebe100;
    --blue: #1f4e96;
    --navy: #0f1d3a;
    --white: #ffffff;
    --stage: #e9ebed;
    --mattress-light: #d9d9d9;
    --mattress-dark: #6e6e6e;
    --map-base: #e7e3da;
    --map-road: #d3cdbf;
  }
  * { box-sizing: border-box; margin: 0; padding: 0; }
  html, body { width: 1200px; height: 700px; overflow: hidden; }
  body {
    background: var(--stage);
    font-family: "Oswald", "Arial Narrow", sans-serif;
    display: flex;
    align-items: center;
    justify-content: center;
    gap: 60px;
  }
  .flyer {
    position: relative;
    width: 464px;
    height: 600px;
    background: var(--white);
    box-shadow: 0 6px 20px rgba(0,0,0,.15);
    overflow: hidden;
  }
  .brand-head {
    background: var(--yellow);
    display: flex;
    align-items: center;
    justify-content: center;
    gap: 12px;
  }
  .brand-mark { width: 18px; height: 18px; background: var(--blue); }
  .brand-name {
    color: var(--blue);
    font-weight: 600;
    text-transform: uppercase;
    letter-spacing: 2px;
  }
  .band {
    background: var(--blue);
    color: var(--white);
    text-transform: uppercase;
    font-weight: 500;
    display: flex;
    align-items: center;
    justify-content: center;
  }

  /* Front */
  .front .brand-head { height: 208px; }
  .front .brand-name { font-size: 40px; }
  .front .tagline {
    height: 62px;
    font-size: 28px;
    border-top: 4px solid var(--white);
    border-bottom: 4px solid var(--white);
    outline: 0;
  }
  .product {
    position: relative;
    height: 180px;
    margin: 8px 48px 0;
  }
  .mattress-photo {
    position: absolute;
    left: 20px; right: 20px; top: 0; height: 120px;
    background: linear-gradient(180deg, var(--mattress-light) 0%, #bdbdbd 55%, var(--mattress-dark) 100%);
    border-radius: 4px;
  }
  .price-list {
    position: absolute;
    left: 0; right: 0; bottom: 0;
    display: grid;
    grid-template-columns: 1fr 1fr;
    row-gap: 0;
    column-gap: 18px;
    color: var(--blue);
    font-size: 31px;
    font-weight: 600;
    line-height: 1.15;
    text-align: center;
    text-transform: uppercase;
  }
  .brand-row {
    margin-top: 10px;
    border-top: 6px solid var(--blue);
    height: 72px;
    display: flex;
    align-items: center;
    justify-content: space-around;
    padding: 0 28px;
  }
  .brand-row span {
    color: var(--blue);
    font-size: 17px;
    font-weight: 500;
  }
  .front .closing {
    background: var(--yellow);
    height: 30px;
    margin-top: 6px;
    color: var(--blue);
    font-size: 13px;
    font-weight: 500;
    text-transform: uppercase;
    display: flex;
    align-items: center;
    justify-content: center;
  }

  /* Back */
  .back .brand-head { height: 138px; }
  .back .brand-name { font-size: 32px; }
  .back .headline {
    height: 58px;
    font-size: 38px;
    font-weight: 600;
  }
  .map-frame {
    margin: 10px 10px 0;
    height: 162px;
    border: 4px solid var(--blue);
  }
  .map {
    width: 100%; height: 100%;
    background: linear-gradient(135deg, var(--map-base) 0%, var(--map-road) 100%);
  }
  .contact {
    position: relative;
    margin-top: 10px;
    height: 118px;
    background: var(--blue);
  }
  .contact svg { position: absolute; left: 0; top: 0; }
  .call-tab {
    position: absolute;
    left: 0; top: 10px;
    padding: 4px 16px 4px 14px;
    background: var(--blue);
    color: var(--white);
    font-size: 20px;
    font-weight: 500;
    text-transform: uppercase;
  }
  .phone {
    position: absolute;
    left: 14px; top: 58px;
    color: var(--blue);
    font-size: 26px;
    font-weight: 600;
  }
  .address {
    position: absolute;
    right: 22px; top: 24px;
    width: 190px;
    color: var(--white);
    font-size: 21px;
    font-weight: 500;
    line-height: 1.4;
    text-transform: uppercase;
  }
  .social {
    height: 60px;
    background: var(--navy);
    display: flex;
    align-items: center;
    justify-content: space-between;
    padding: 0 22px 0 56px;
  }
  .social-names {
    color: var(--white);
    font-size: 15px;
    font-weight: 500;
  }
  .social-links {
    color: var(--white);
    font-size: 9px;
    line-height: 1.6;
    text-transform: uppercase;
    text-align: left;
  }
  .back .closing {
    background: var(--yellow);
    height: 24px;
    color: var(--blue);
    font-size: 14px;
    font-weight: 600;
    text-transform: uppercase;
    display: flex;
    align-items: center;
    justify-content: center;
  }
</style>
</head>
<body>

  <section class="flyer front">
    <header class="brand-head">
      <span class="brand-mark"></span>
      <span class="brand-name">Coral Rest Outlet</span>
    </header>
    <div class="band tagline">Lowest Prices. Best Brands.</div>
    <div class="product">
      <div class="mattress-photo" role="img" aria-label="Photo of a grey quilted mattress on a box spring"></div>
      <div class="price-list">
        <span>Twin - $99</span>
        <span>Full - $159</span>
        <span>Queen - $199</span>
        <span>King - $299</span>
      </div>
    </div>
    <div class="brand-row">
      <span>Quillard</span>
      <span>Dravo</span>
      <span>Velmora</span>
      <span>brook &amp; vantle</span>
    </div>
    <div class="closing">And other great brand names!</div>
  </section>

  <section class="flyer back">
    <header class="brand-head">
      <span class="brand-mark"></span>
      <span class="brand-name">Coral Rest Outlet</span>
    </header>
    <div class="band headline">Contact Us Now!</div>
    <div class="map-frame">
      <div class="map" role="img" aria-label="Street map showing the store location at 24315 SW 142nd St, Miami"></div>
    </div>
    <div class="contact">
      <svg width="464" height="118" viewBox="0 0 464 118" aria-hidden="true">
        <polygon points="0,0 150,0 192,118 0,118" fill="var(--yellow)"/>
      </svg>
      <div class="call-tab">Call Us!</div>
      <div class="phone">(786)413-9072</div>
      <div class="address">24315 SW 142nd St,<br>Miami, FL 33157, USA</div>
    </div>
    <div class="social">
      <span class="social-names">Friendsnet · Circlely · Chirpline</span>
      <div class="social-links">
        https://www.friendsnet.com/coralrestoutlet<br>
        https://www.circlely.com/+coralrestoutlet<br>
        https://chirpline.com/coralrestoutlet
      </div>
    </div>
    <div class="closing">http://www.coralrestoutlet.com/</div>
  </section>

</body>
</html>
```